Website Upgrade

Create new look for existing website: www.lunarisgrove.ca . You will find details on what we are about on the website. Email us at lunaris.grove@mailbright.ca if you have any questions. We will be more than happy to answer.
Lunaris grove is a website for women focused on empowering women.
Website must:
1. Be able to stream videos
2. Use of blogs
3. Purple must be one of the colours used in the scheme.
4. Must use existing lunaris grove logo (purple head with 'Lunaris Grove' script in white.. see on homepage). However, we are open to new logo suggestions
5. Must be professional. We are trendy but not boring.

```html
<!DOCTYPE html>
<html lang="en">
<head>
<meta charset="utf-8">
<title>Lunaris Grove</title>
<link href="https://fonts.googleapis.com/css2?family=Varela+Round&family=Open+Sans:wght@400;600&display=swap" rel="stylesheet">
<style>
  :root {
    --purple: #8e2aa6;
    --purple-deep: #6a1f86;
    --nav-top: #a44bc0;
    --nav-bottom: #7a2596;
    --magenta: #9a1b82;
    --ink: #1b1b1b;
    --text: #6a6a6a;
    --muted: #8a8a8a;
    --line: #e4e4e4;
    --footer-bg: #f7f6f8;
    --white: #ffffff;
  }
  * { box-sizing: border-box; margin: 0; padding: 0; }
  html, body { width: 892px; height: 1200px; overflow: hidden; background: var(--white); }
  body { font-family: "Open Sans", Arial, sans-serif; color: var(--text); position: relative; }

  .site-header { position: absolute; top: 0; left: 0; width: 892px; height: 83px; }
  .brand { position: absolute; left: 113px; top: 22px; display: flex; align-items: center; gap: 8px; }
  .brand-mark { width: 26px; height: 26px; border-radius: 50%; background: var(--purple); }
  .brand-name { font-family: "Varela Round", sans-serif; font-size: 22px; color: var(--magenta); letter-spacing: 0.5px; }
  .social { position: absolute; right: 111px; top: 56px; display: flex; gap: 5px; }
  .social span { width: 15px; height: 15px; border-radius: 2px; }
  .social .s1 { background: #3b5b99; } .social .s2 { background: #55b7e6; } .social .s3 { background: #1f73a8; }

  .main-nav { position: absolute; top: 83px; left: 0; width: 892px; height: 36px;
    background: linear-gradient(var(--nav-top), var(--nav-bottom)); display: flex; padding-left: 124px; }
  .main-nav a { font-family: "Varela Round", sans-serif; color: var(--white); text-decoration: none; font-size: 12px;
    line-height: 36px; padding: 0 18px; border-right: 1px solid rgba(255,255,255,0.25); }
  .main-nav a:last-child { border-right: none; }

  .hero { position: absolute; top: 119px; left: 0; width: 892px; height: 322px;
    background: linear-gradient(90deg, #f4f4f6, #fafafa 40%, #f2f2f4); border-bottom: 1px solid var(--line); overflow: hidden; }
  .hero-photo { position: absolute; left: 320px; top: 0; width: 480px; height: 322px;
    background: linear-gradient(100deg, rgba(244,244,246,0) 0%, #dcd8da 22%, #8a7f80 45%, #3e3b42 65%, #6e6a72 82%, #ececef 100%); }
  .hero-copy { position: absolute; left: 113px; top: 76px; width: 280px; }
  .hero-title { font-family: "Varela Round", sans-serif; font-size: 21px; line-height: 30px; color: var(--ink); letter-spacing: 0.3px; }
  .hero-title .accent { color: var(--magenta); font-size: 18px; }
  .hero-text { font-size: 9.5px; line-height: 15px; margin-top: 6px; color: var(--text); width: 270px; }
  .btn { display: inline-block; margin-top: 9px; width: 98px; height: 24px; border-radius: 2px; background: var(--purple-deep);
    color: var(--white); font-family: "Varela Round", sans-serif; font-size: 9px; line-height: 24px; text-align: center; }
  .dots { display: flex; gap: 2px; margin-top: 9px; }
  .dots span { width: 9px; height: 9px; border-radius: 50%; background: #6d6d6d; }

  .intro { position: absolute; top: 476px; left: 0; width: 892px; text-align: center; }
  .intro h1 { font-family: "Varela Round", sans-serif; font-weight: 400; font-size: 25px; color: var(--purple); }
  .intro h2 { font-family: "Varela Round", sans-serif; font-weight: 400; font-size: 13px; color: #555; margin-top: 11px; }
  .intro p { font-size: 8.3px; line-height: 14.5px; width: 630px; margin: 13px auto 0; color: var(--text); }

  .videos { position: absolute; top: 590px; left: 0; width: 892px; height: 250px;
    background: linear-gradient(var(--white) 70%, #f6f6f8); }
  .video-card { position: absolute; top: 40px; width: 166px; }
  .video-thumb { position: relative; width: 163px; height: 104px; border: 3px solid var(--white); box-shadow: 0 0 2px rgba(0,0,0,0.25); }
  .video-thumb .fill { width: 100%; height: 100%; }
  .play { position: absolute; left: 50%; top: 50%; width: 22px; height: 22px; margin: -11px 0 0 -11px; border-radius: 50%; background: var(--white); }
  .play svg { display: block; }
  .video-card h3 { font-family: "Varela Round", sans-serif; font-weight: 400; font-size: 12.5px; color: #333; margin-top: 11px; }
  .video-card p { font-size: 7.5px; line-height: 13px; color: var(--muted); margin-top: 3px; width: 150px; }

  .recent-blog { position: absolute; top: 864px; left: 0; width: 892px; }
  .recent-blog h2 { position: absolute; left: 114px; top: 0; font-family: "Varela Round", sans-serif; font-weight: 400; font-size: 18px; color: var(--purple-deep); }
  .post { position: absolute; width: 330px; height: 72px; }
  .post-img { position: absolute; left: 0; top: 0; width: 123px; height: 70px; }
  .post-body { position: absolute; left: 134px; top: -2px; width: 190px; }
  .post-body h3 { font-family: "Varela Round", sans-serif; font-weight: 400; font-size: 11.5px; color: #333; white-space: nowrap; }
  .post-body p { font-size: 8.2px; line-height: 13.5px; color: var(--muted); margin-top: 4px; }
  .post-body a { font-size: 8.2px; color: var(--purple-deep); text-decoration: none; display: block; margin-top: 3px; }

  .site-footer { position: absolute; top: 1114px; left: 0; width: 892px; height: 86px; background: var(--footer-bg); }
  .footer-nav { position: absolute; left: 114px; top: 22px; font-family: "Varela Round", sans-serif; font-size: 11px; color: var(--purple-deep); }
  .footer-nav a { color: var(--purple-deep); text-decoration: none; }
  .footer-nav .sep { margin: 0 4px; color: #555; }
  .copyright { position: absolute; left: 114px; top: 46px; font-size: 8.3px; color: var(--text); }
</style>
</head>
<body>
  <header class="site-header">
    <div class="brand"><span class="brand-mark"></span><span class="brand-name">Lunaris Grove</span></div>
    <div class="social"><span class="s1"></span><span class="s2"></span><span class="s3"></span></div>
  </header>

  <nav class="main-nav">
    <a href="#">HOME</a><a href="#">ABOUT US</a><a href="#">LUNARIS GROVE</a><a href="#">FAQ</a><a href="#">OUR BLOGS</a><a href="#">CONTACT US</a>
  </nav>

  <section class="hero">
    <div class="hero-photo" role="img" aria-label="Portrait photo of a woman with long dark wavy hair on a light background"></div>
    <div class="hero-copy">
      <div class="hero-title"><span class="accent">EMBODY YOUR RADIANCE,</span><br>MAGNETISM, AND<br>FEMININE POWER NOW</div>
      <p class="hero-text">Suspendisse vulputate aliquam dui Nulla elementum dui ut augue Aliquam vehicula mi at mauris Maecena</p>
      <span class="btn">READ MORE</span>
      <div class="dots"><span></span><span></span><span></span><span></span></div>
    </div>
  </section>

  <section class="intro">
    <h1>Mauris vel lacus vitae felis vestibulum</h1>
    <h2>Morbi eget arcu Morbi porta libero id ullamcorper nonummy nibh ligula pulvinar metus</h2>
    <p>Vivamus porttitor g purus nisi eleifend libero a tempus libero lectus feugiat felis Morbi diam mauris viverra in gravida eu mattis in ante Morbi eget arcu Morbi porta libero id ullamcorper nonummy nibh ligula pulvinar metus eget consectetuer augue nisi quis lacus Ut ac mi quis lacus mollis aliquam Curabitur iaculis tempus eros Curabitur vel mi sit amet magna malesuada ultrices Ut nisi erat fermentum vel congue</p>
  </section>

  <section class="videos">
    <article class="video-card" style="left:112px">
      <div class="video-thumb"><div class="fill" role="img" aria-label="Woman in a purple top sitting outdoors under a blue sky" style="background:linear-gradient(#9fc0e0,#c9d9ec 55%,#8a4a9e)"></div>
        <span class="play"><svg width="22" height="22" viewBox="0 0 22 22"><path d="M9 6.5 L15.5 11 L9 15.5Z" fill="#111"/></svg></span></div>
      <h3>Video Tittle</h3>
      <p>Morbi eget arcu Morbi porta libero id ullamcorper nonummy nibh lig</p>
    </article>
    <article class="video-card" style="left:284px">
      <div class="video-thumb"><div class="fill" role="img" aria-label="Smiling blonde woman by the sea" style="background:linear-gradient(90deg,#f1e8dc,#e4d2b6 45%,#bcdcef)"></div>
        <span class="play"><svg width="22" height="22" viewBox="0 0 22 22"><path d="M9 6.5 L15.5 11 L9 15.5Z" fill="#111"/></svg></span></div>
      <h3>Video Tittle</h3>
      <p>Morbi eget arcu Morbi porta libero id ullamcorper nonummy</p>
    </article>
    <article class="video-card" style="left:454px">
      <div class="video-thumb"><div class="fill" role="img" aria-label="Swimmer underwater in a bright blue pool" style="background:linear-gradient(#7fd2ea,#1d8fc0 50%,#0a5f93)"></div>
        <span class="play"><svg width="22" height="22" viewBox="0 0 22 22"><path d="M9 6.5 L15.5 11 L9 15.5Z" fill="#111"/></svg></span></div>
      <h3>Video Tittle</h3>
      <p>Morbi eget arcu Morbi porta libero id ullamcorper nonummy</p>
    </article>
    <article class="video-card" style="left:626px">
      <div class="video-thumb"><div class="fill" role="img" aria-label="Collage of a woman's portrait in soft grey tiles" style="background:linear-gradient(90deg,#e8e8ea,#cfc8c4 50%,#dde4ea)"></div>
        <span class="play"><svg width="22" height="22" viewBox="0 0 22 22"><path d="M9 6.5 L15.5 11 L9 15.5Z" fill="#111"/></svg></span></div>
      <h3>Video Tittle</h3>
      <p>Morbi eget arcu Morbi porta libero id ullamcorper nonummy nibh lig</p>
    </article>
  </section>

  <section class="recent-blog">
    <h2>RECENT BLOG</h2>
    <article class="post" style="left:114px;top:37px">
      <div class="post-img" role="img" aria-label="Athletic woman in sportswear against a dark wall" style="background:linear-gradient(90deg,#3a3a3e,#6a6a6e 50%,#2f2f33)"></div>
      <div class="post-body"><h3>Donec scelerisque leo ac risus</h3><p>Morbi porta libero id ullamcorper nonummy nibh ligula pulvinar metus eget consectetuer augue nisi quis lacus Ut ac mi</p><a href="#">Read full story</a></div>
    </article>
    <article class="post" style="left:463px;top:37px">
      <div class="post-img" role="img" aria-label="Smiling woman with dark hair on a warm sand background" style="background:linear-gradient(90deg,#e2c58f,#8a5a3e 50%,#e6cc98)"></div>
      <div class="post-body"><h3>Donec scelerisque leo ac risus</h3><p>Morbi porta libero id ullamcorper nonummy nibh ligula pulvinar metus eget consectetuer augue nisi quis lacus Ut ac mi</p><a href="#">Read full story</a></div>
    </article>
    <article class="post" style="left:114px;top:133px">
      <div class="post-img" role="img" aria-label="Smiling woman in a blue top among sunny greenery" style="background:linear-gradient(90deg,#c9d44a,#efe7a0 45%,#3a7fc7 80%,#b7c94c)"></div>
      <div class="post-body"><h3>Donec scelerisque leo ac risus</h3><p>Morbi porta libero id ullamcorper nonummy nibh ligula pulvinar metus eget consectetuer augue nisi quis lacus Ut ac mi</p><a href="#">Read full story</a></div>
    </article>
    <article class="post" style="left:463px;top:133px">
      <div class="post-img" role="img" aria-label="Woman relaxing on white spa towels" style="background:linear-gradient(#c9b4a4,#e9ddd3 55%,#f4f1ee)"></div>
      <div class="post-body"><h3>Donec scelerisque leo ac risus</h3><p>Morbi porta libero id ullamcorper nonummy nibh ligula pulvinar metus eget consectetuer augue nisi quis lacus Ut ac mi</p><a href="#">Read full story</a></div>
    </article>
  </section>

  <footer class="site-footer">
    <div class="footer-nav"><a href="#">HOME</a><span class="sep">|</span><a href="#">ABOUT US</a><span class="sep">|</span><a href="#">LUNARIS GROVE</a><span class="sep">|</span><a href="#">FAQ</a><span class="sep">|</span><a href="#">OUR BLOGS</a><span class="sep">|</span><a href="#">CONTACT US</a></div>
    <p class="copyright">© 2014 Company Name &nbsp;All right reserved &nbsp;Term of Use</p>
  </footer>
</body>
</html>
```